CPA Graduation Party

I need to make simple invitation for my sister's recent success, passing the CPA (Certified Public Accountant) exam. It is a surprise party. I want very simple and professional looking invitation. My only requirements are that you don't use any graduation caps or gowns due to the fact that it's not an actual graduation. It's a series of exams that she passes. Be creative with the design but once again, keep it professional. I have attached a font called iScriptSTD. I liked the font so was thinking about using it. But it's not necessary. If you have something slimier or better, please use it.

I was planning on printing on a specific kind of paper. It's called pearlized ivory cardstock. It has a little coating and shine on it and since it's ivory, I was thinking about the main color of the invitation to be burgundy type. For example, see the following RGB: R204, G0, B102.

Party info:
Name: Ravina
Date & Time: Saturday, March 8th, 2014 at 6:00pm
Location: Seher Mahal. 418 Brambleford Lane Parsippany, NJ 07291

I know I didn't provide a lot of info for the invite but please be creative.  Use general knowledge and other formal party invites as examples. I am not looking for a name, date and location as three bullets on the card.

Also, I forgot to mention the size of the invite.  It should be 5.5x8.5.  Thank you.

• graduation caps and/or gowns

```html
<!DOCTYPE html>
<html lang="en">
<head>
<meta charset="utf-8">
<title>Graduation Celebration – Ravina, CPA</title>
<link rel="stylesheet" href="https://fonts.googleapis.com/css2?family=Kalam:wght@700&display=swap">
<style>
  :root {
    --backdrop: #e7e3da;
    --cardstock: #f2eedb;
    --ribbon: #cc0a69;
    --ink: #111111;
    --party-warm: #f4c98a;
    --party-cool: #e7a6c8;
  }
  * { margin: 0; padding: 0; box-sizing: border-box; }
  html, body {
    width: 1200px;
    height: 1000px;
    overflow: hidden;
    background: var(--backdrop);
  }
  .invitation {
    position: absolute;
    left: 242px;
    top: 30px;
    width: 712px;
    height: 938px;
    background: var(--cardstock);
    font-family: "Kalam", "Comic Sans MS", cursive;
    font-weight: 700;
    color: var(--ink);
    overflow: hidden;
  }
  .ribbon { position: absolute; background: var(--ribbon); }
  .ribbon--vertical { left: 78px; top: 0; width: 61px; height: 100%; }
  .ribbon--horizontal { left: 0; top: 94px; width: 100%; height: 61px; }
  .invitation__title {
    position: absolute;
    left: 176px;
    top: 22px;
    font-size: 47px;
    line-height: 1.2;
    letter-spacing: 0.8px;
    white-space: nowrap;
  }
  .details {
    position: absolute;
    left: 188px;
    top: 240px;
    font-size: 28px;
    line-height: 38px;
    letter-spacing: -0.2px;
  }
  .details__row { display: flex; margin-bottom: 22px; }
  .details__label { width: 226px; }
  .details__value { white-space: nowrap; }
  .party-art {
    position: absolute;
    left: 190px;
    top: 680px;
    width: 486px;
    height: 240px;
    border-radius: 40px;
    background: radial-gradient(ellipse at 50% 60%, var(--party-warm), var(--party-cool) 60%, var(--cardstock) 100%);
    opacity: 0.7;
  }
</style>
</head>
<body>
  <main class="invitation">
    <div class="ribbon ribbon--vertical"></div>
    <div class="ribbon ribbon--horizontal"></div>

    <h1 class="invitation__title">Graduation Celebration</h1>

    <dl class="details">
      <div class="details__row">
        <dt class="details__label">Honouring:</dt>
        <dd class="details__value">Ravina, CPA</dd>
      </div>
      <div class="details__row">
        <dt class="details__label">Date:</dt>
        <dd class="details__value">Saturday, 8th March</dd>
      </div>
      <div class="details__row">
        <dt class="details__label">Time:</dt>
        <dd class="details__value">6.00 p.m</dd>
      </div>
      <div class="details__row">
        <dt class="details__label">Place:</dt>
        <dd class="details__value">Seher Mahal.<br>418 Brambleford Lane,<br>Parsippany,<br>NJ 07291</dd>
      </div>
    </dl>

    <div class="party-art" role="img" aria-label="Cartoon party guests in party hats celebrating among confetti and streamers"></div>
  </main>
</body>
</html>
```